Real Estate Agent need For Sale sign for

We need a for sale sign for our team based in Los Angeles, CA. My team name is Corvalen Real Estate Group. Also known as Team Corvalen. We are also under the Brandt Osgood umbrella. We are a real estate team that enjoys contributing to the world through supporting homeowners and sellers achieve their real estate goals. The final design should communicate trust, integrity, and loyalty.
Need to have our team name on there: Team Corvalen, phone number 323-555-0172, my licensed number DRE #8062714 on there. The size of the sign will be 32X36.
Target Market(s)
Home buyers and sellers.
Industry/Entity Type
Real Estate Agent
Colors
Designer to choose colors to be used in the design.
Look and feel

```html
<!DOCTYPE html>
<html lang="en">
<head>
<meta charset="utf-8">
<title>Team Corvalen – For Sale Sign</title>
<link rel="stylesheet" href="https://fonts.googleapis.com/css2?family=Saira:wght@600&family=Arimo:wght@400&display=swap">
<style>
  :root {
    --sign-blue: #0d57a5;
    --brand-blue: #0d57a5;
    --paper: #ffffff;
    --ink: #333333;
    --partner-ink: #555555;
  }
  * { margin: 0; padding: 0; box-sizing: border-box; }
  html, body { width: 1067px; height: 1200px; overflow: hidden; }
  body { background: var(--sign-blue); }
  .sign {
    position: relative;
    width: 1067px;
    height: 1200px;
    background: var(--sign-blue);
    font-family: "Saira", "Arial", sans-serif;
  }
  .brand-box {
    position: absolute;
    left: 336px; top: 111px;
    width: 395px; height: 248px;
    background: var(--paper);
    display: flex;
    flex-direction: column;
    align-items: center;
    justify-content: center;
    gap: 6px;
    color: var(--brand-blue);
    font-weight: 600;
    text-transform: uppercase;
    text-align: center;
  }
  .brand-mark {
    width: 34px; height: 34px;
    background: var(--brand-blue);
    margin-bottom: 8px;
  }
  .brand-name { font-size: 58px; line-height: 1; letter-spacing: 1px; }
  .brand-sub { font-size: 24px; line-height: 1; letter-spacing: 2px; }
  .team-name {
    position: absolute;
    left: 0; right: 0; top: 418px;
    color: var(--paper);
    font-weight: 600;
    text-align: center;
    text-transform: uppercase;
    line-height: 1;
  }
  .team-name .line { display: block; }
  .team-name .line-team { font-size: 172px; }
  .team-name .line-name { font-size: 156px; margin-top: 22px; }
  .partner-box {
    position: absolute;
    left: 425px; top: 809px;
    width: 217px; height: 136px;
    background: var(--paper);
    display: flex;
    flex-direction: column;
    align-items: center;
    padding-top: 12px;
  }
  .partner-intro {
    font-family: "Arimo", "Arial", sans-serif;
    font-size: 17px;
    color: var(--ink);
  }
  .partner-name {
    margin-top: 26px;
    font-size: 28px;
    font-weight: 600;
    color: var(--partner-ink);
    line-height: 1;
  }
  .contact-band {
    position: absolute;
    left: 0; top: 1035px;
    width: 1067px; height: 52px;
    background: var(--paper);
    display: flex;
    align-items: center;
    justify-content: space-between;
    padding: 0 61px 0 60px;
    font-family: "Arimo", "Arial", sans-serif;
    font-size: 26px;
    color: var(--brand-blue);
  }
</style>
</head>
<body>
  <main class="sign">
    <div class="brand-box">
      <div class="brand-mark"></div>
      <div class="brand-name">Corvalen</div>
      <div class="brand-sub">Real Estate Group</div>
    </div>

    <h1 class="team-name">
      <span class="line line-team">Team</span>
      <span class="line line-name">Corvalen</span>
    </h1>

    <div class="partner-box">
      <p class="partner-intro">We are also under the</p>
      <p class="partner-name">Brandt Osgood</p>
    </div>

    <div class="contact-band">
      <span class="license">Licensed Number - &nbsp;DRE #8062714</span>
      <span class="phone">Phone Number - 323-555-0172</span>
    </div>
  </main>
</body>
</html>
```